Castastrophe General Contractor needs leave behind for sales

Will respond quickly to designer inquires
Fast winning selection
Will notify all of winning selection

Catastrophe Restoration General Contractor offering specialized services to the insurance industry. Sales meeting leave behind flyer for presentation to insurance agents. We would like for agents to refer policyholders to our company for complete residential and commercial restoration projects.

Some copy uploaded for reference. 5.5" x 8.5" approx - double sided color w/ sales business card reproduced on back side. Approved / Preferred Contractor for Brightshield, Vantacover, KRPQ & Fenlo insurance companies.

Larkmoor Company is a general contractor specialized in the restoration industry for both residential and commercial properties.
We have incorporated the best technology tools and partnered with a network of industry professionals across the country to provide the most efficient and comprehensive service available.
Website under construction: www.thelarkmoorcompany.example

Target Market(s)

Insurance Sale Agents

Industry/Entity Type

Residential

Requirements
Must have
• Brightshield, Vantacover & KRPQ & Halvey Dresmit logos. Space to reproduce business card on back.. Looking for concept deign where we can work w/ local designer if necessary to finalize. Open to different sized flyer dependent on design.

```html
<!DOCTYPE html>
<html lang="en">
<head>
<meta charset="utf-8">
<title>Larkmoor Company – Agent Leave-Behind Flyer</title>
<link rel="stylesheet" href="https://fonts.googleapis.com/css2?family=Open+Sans:wght@400;600;700;800&display=swap">
<style>
  :root{
    --teal:#2a6f83;
    --teal-deep:#1f5b6c;
    --teal-light:#5f97a8;
    --orange:#f2a93b;
    --white:#ffffff;
    --paper:#e8e9ea;
    --ink:#1f4f5e;
    --muted:#d8e6ea;
  }
  *{box-sizing:border-box;margin:0;padding:0}
  html,body{width:1200px;height:1000px;overflow:hidden}
  body{background:var(--paper);font-family:"Open Sans",Arial,sans-serif;color:var(--ink);position:relative}

  .flyer{position:absolute;left:250px;width:700px;height:453px;overflow:hidden;box-shadow:0 6px 18px rgba(0,0,0,.18)}
  .flyer--front{top:30px;background:var(--white)}
  .flyer--back{top:515px;background:radial-gradient(ellipse 60% 70% at 50% 42%,var(--teal-light) 0%,var(--teal) 60%,var(--teal-deep) 100%)}

  /* brand lockup */
  .brand{display:flex;align-items:center;gap:7px;font-weight:700;letter-spacing:.12em;text-transform:uppercase}
  .brand__mark{width:12px;height:12px;background:currentColor}

  /* front: header */
  .front-header{position:absolute;top:0;left:0;right:0;height:162px}
  .front-header .brand{position:absolute;top:16px;left:0;right:0;justify-content:center;color:var(--teal);font-size:13px}
  .tagline-band{position:absolute;top:44px;left:0;width:500px;height:16px;background:var(--orange);color:var(--white);font-size:9.5px;font-weight:700;letter-spacing:.25em;line-height:16px;padding-left:24px}
  .support{position:absolute;top:67px;left:24px;width:470px}
  .support__title{font-size:11.5px;font-weight:800;color:var(--teal-deep);line-height:1.3}
  .support__sub{font-size:10.5px;font-weight:700;color:var(--teal-deep);margin-top:6px}
  .support__list{list-style:none;font-size:8.5px;line-height:1.35;color:var(--ink);margin-top:1px}
  .support__list li::before{content:"• "}

  /* front: benefits */
  .benefits{position:absolute;top:162px;left:0;right:0;height:233px;background:var(--teal);color:var(--white)}
  .benefits__title{position:absolute;top:8px;left:0;right:0;text-align:center;font-size:22px;font-weight:700}
  .benefits__links{position:absolute;inset:0}
  .benefit{position:absolute;top:60px;width:200px;text-align:center}
  .benefit--satisfaction{left:20px}
  .benefit--efficiency{left:250px}
  .benefit--quality{left:480px}
  .benefit__icon{display:block;margin:0 auto 6px}
  .benefit__name{font-size:11px;font-weight:700;line-height:1.25}
  .benefit__text{font-size:8px;line-height:1.4;margin-top:5px;color:var(--muted)}
  .benefits__web{position:absolute;right:24px;bottom:8px;font-size:9.5px;font-weight:600;letter-spacing:.22em}

  /* front: partners */
  .partners-tab{position:absolute;left:0;top:395px;width:130px;height:15px;background:var(--orange);color:var(--white);font-size:9px;font-weight:700;letter-spacing:.25em;line-height:15px;padding-left:18px;z-index:2}
  .partners{position:absolute;left:0;right:0;bottom:0;height:43px;display:flex;align-items:center;justify-content:space-around;padding:0 12px}
  .partner{display:flex;align-items:center;gap:5px;font-size:10px;font-weight:700;color:var(--teal-deep);white-space:nowrap}
  .partner__box{width:10px;height:10px;border:1.5px solid var(--teal-deep)}
  .badge{width:26px;height:26px;border-radius:50%;background:var(--teal-deep)}
  .badge--square{border-radius:2px;width:20px;height:26px;background:var(--teal)}
  .mascot{width:28px;height:26px;border-radius:6px;background:linear-gradient(135deg,#f3b6cf,#e88fb4)}

  /* back */
  .back-brand{position:absolute;top:190px;left:0;right:0;justify-content:center;color:var(--white);font-size:15px}
  .contact-panel{position:absolute;left:0;bottom:0;width:420px;height:120px;background:var(--white);clip-path:polygon(0 0,330px 0,420px 100%,0 100%)}
  .contact{position:absolute;left:28px;top:22px;color:var(--teal-deep);font-size:12px;line-height:1.55}
  .contact__row{display:flex;align-items:center;gap:7px}
  .contact__web{font-size:15px;letter-spacing:.22em;margin-top:6px}
  .back-partners{position:absolute;right:30px;bottom:22px;width:250px;display:flex;flex-wrap:wrap;gap:8px 14px;justify-content:flex-end;align-items:center;opacity:.45}
  .back-partners .partner{color:var(--teal-deep)}
</style>
</head>
<body>

<section class="flyer flyer--front" aria-label="Flyer front">
  <header class="front-header">
    <div class="brand"><span class="brand__mark"></span>Larkmoor Company</div>
    <div class="tagline-band">Your National Restoration Contractor</div>
    <div class="support">
      <p class="support__title">Preferred Contractor Agent Support<br>Providing claims support during and after a CAT event</p>
      <p class="support__sub">Agent Support Services</p>
      <ul class="support__list">
        <li>Guaranteed next day inspections from time of notification</li>
        <li>Claim status reporting directly back to Agent</li>
        <li>Assist policy holder in filing claim to CAT desk</li>
      </ul>
    </div>
  </header>

  <div class="benefits">
    <svg class="benefits__links" width="700" height="233" viewBox="0 0 700 233" aria-hidden="true">
      <path d="M120 52 V36 H580 V52 M350 36 V52" fill="none" stroke="#ffffff" stroke-width="1.5" stroke-dasharray="2 4"/>
      <line x1="233" y1="85" x2="233" y2="190" stroke="#ffffff" stroke-opacity=".35"/>
      <line x1="467" y1="85" x2="467" y2="190" stroke="#ffffff" stroke-opacity=".35"/>
    </svg>
    <h2 class="benefits__title">Agent Benefits:</h2>

    <div class="benefit benefit--satisfaction">
      <svg class="benefit__icon" width="26" height="26" viewBox="0 0 24 24" aria-hidden="true"><path d="M2 10h4v11H2zM8 21V10l5-8c1.6 0 2.5 1 2.2 2.6L14.5 9H21c1.1 0 2 1 1.8 2.1l-1.5 8.2c-.2 1-1 1.7-2 1.7z" fill="#ffffff"/></svg>
      <p class="benefit__name">Greater Satisfaction,<br>Increased Retention</p>
      <p class="benefit__text">Increase policyholder satisfaction • Demonstrate a greater commitment to customer satisfaction • Follow up on outcome beyond the closing of a claim</p>
    </div>

    <div class="benefit benefit--efficiency">
      <svg class="benefit__icon" width="40" height="26" viewBox="0 0 40 26" aria-hidden="true">
        <g fill="none" stroke="#ffffff" stroke-width="2.5">
          <circle cx="12" cy="14" r="6"/><circle cx="12" cy="14" r="2"/>
          <circle cx="28" cy="12" r="7"/><circle cx="28" cy="12" r="2.5"/>
        </g>
        <g stroke="#ffffff" stroke-width="3" stroke-dasharray="2 2.7"><circle cx="12" cy="14" r="8" fill="none"/><circle cx="28" cy="12" r="9" fill="none"/></g>
      </svg>
      <p class="benefit__name">Enhanced Efficiency</p>
      <p class="benefit__text">Increase efficiency in moving from claim to restoration completion • In-house systems closely linked to the insurer or administrator • Shorten the timeline from claims settlement to finished repairs</p>
    </div>

    <div class="benefit benefit--quality">
      <svg class="benefit__icon" width="26" height="26" viewBox="0 0 26 26" aria-hidden="true">
        <circle cx="13" cy="13" r="11.5" fill="none" stroke="#ffffff" stroke-width="2"/>
        <circle cx="13" cy="13" r="7.5" fill="#ffffff"/>
        <path d="M9.5 13l2.5 2.5 4.5-5" fill="none" stroke="#2a6f83" stroke-width="2"/>
      </svg>
      <p class="benefit__name">Increased Quality Control</p>
      <p class="benefit__text">Pre-screened and credentialed for license, insurance, and financial stability • Monitored performance and control standards for higher quality outcomes • Background verification on all staff and field representatives</p>
    </div>

    <p class="benefits__web">www.thelarkmoorcompany.example</p>
  </div>

  <div class="partners-tab">Our Partners</div>
  <div class="partners">
    <span class="partner"><span class="partner__box"></span>Brightshield</span>
    <span class="badge badge--square" role="img" aria-label="Accredited business listing badge"></span>
    <span class="partner">Vantacover</span>
    <span class="partner"><span class="partner__box"></span>KRPQ</span>
    <span class="badge" role="img" aria-label="Restoration association badge"></span>
    <span class="badge" role="img" aria-label="Certification badge"></span>
    <span class="partner">Fenlo</span>
    <span class="partner"><span class="partner__box"></span>Halvey Dresmit Preferred Contractor</span>
    <span class="mascot" role="img" aria-label="Partner mascot character"></span>
  </div>
</section>

<section class="flyer flyer--back" aria-label="Flyer back">
  <div class="brand back-brand"><span class="brand__mark"></span>Larkmoor Company</div>

  <div class="contact-panel">
    <div class="contact">
      <p class="contact__row">
        <svg width="12" height="12" viewBox="0 0 24 24" aria-hidden="true"><circle cx="12" cy="12" r="11" fill="none" stroke="#1f5b6c" stroke-width="2"/><path d="M8 6l2 .3 1 3-1.5 1.2a8 8 0 0 0 4 4L15 13l3 1 .3 2-1.3 1.5C11 18 6 13 6.5 7.3z" fill="#1f5b6c"/></svg>
        (800) 555-0148
      </p>
      <p class="contact__row">
        <svg width="12" height="10" viewBox="0 0 24 18" aria-hidden="true"><rect x="1" y="1" width="22" height="16" fill="none" stroke="#1f5b6c" stroke-width="2"/><path d="M1 1l11 9 11-9" fill="none" stroke="#1f5b6c" stroke-width="2"/></svg>
        info@larkmoorcompany.example
      </p>
      <p class="contact__web">www.thelarkmoorcompany.example</p>
    </div>
  </div>

  <div class="back-partners">
    <span class="partner"><span class="partner__box"></span>Brightshield</span>
    <span class="badge badge--square" role="img" aria-label="Accredited business listing badge"></span>
    <span class="badge" role="img" aria-label="Certification badge"></span>
    <span class="partner">Fenlo</span>
    <span class="partner">Vantacover</span>
    <span class="partner"><span class="partner__box"></span>KRPQ</span>
    <span class="badge" role="img" aria-label="Restoration association badge"></span>
    <span class="partner"><span class="partner__box"></span>Halvey Dresmit Preferred Contractor</span>
    <span class="mascot" role="img" aria-label="Partner mascot character"></span>
  </div>
</section>

</body>
</html>
```